Banner Ad Design Project

We are re-branding our energy management company called 'Voltrix'. We sell Energy Management Information Software and are currently positioned as a very technical organization. While we are always going to be very technical we want to shift away from telling people about the power of our software and become a more customer centric organization focusing on how energy management can solve many of your organizations problems. The final design should be modern and simple, as we are taking something very technical and complicated and trying to sell it. We need 4 banners created for our site www.voltrix-example.com which rotate across the top. They all need to be different and easily editable (preferably Photoshop)as we change marketing campaigns, the text needs to be editable.

The Size of the banners are 940 pixels by 250 pixels.
Updates

Thank you so much to everyone for you questions and for the few designs I have received. I am very new at this so please if there are things I can do to help better convey my design needs please let me know. Many people have asked for the Text to do on the banners. Here is what I have come up with for the 4 banners.

Banner 1

Maintain high building standards
                - With lower energy costs

Banner 2
Energy Reporting Requirements
                - Made effortless

Banner 3
Presenting Colin Parsons, President of RDLMS, June 19th
- The future of Ontario’s power market

Banner 4
Working with utilities to develop and execute successful Energy Conservation Programs

As well we are working on re-branding ourselves so the website at this point does not convey the look and feel we are looking to go with. The attached files, especially the brochure and business card, convey the look and feel I am looking fore much better!

Reason: Need to check with the rest of my team to make final decision. Keep submitting designs, Thanks!

Industry/Entity Type

Marketing

Requirements
Must have
• The size needs to be 940 by 250 pixels. They need to contain the green color indicated in the 'Voltrix branding design features' document.

Needs to be consistent withe the look and feel of the brochure, PowerPoint and business card attached.

The integration of the 'Voltrix Head' and other similar graphics into the banners.
Should not have
• The look and feel of our current website

```html
<!DOCTYPE html>
<html lang="en">
<head>
<meta charset="UTF-8">
<title>Voltrix Banner – Maintain High Building Standards</title>
<link rel="stylesheet" href="https://fonts.googleapis.com/css2?family=Roboto+Slab:wght@400&family=Carlito:wght@700&display=swap">
<style>
  :root {
    --stage-bg: #212121;
    --brand-green: #82be44;
    --deep-green: #0f5a2e;
    --line-green: #2f5b2a;
    --text-white: #ffffff;
    --art-light: #8fc655;
    --art-dark: #74ad3b;
  }
  html, body {
    margin: 0;
    padding: 0;
    width: 1200px;
    height: 900px;
    overflow: hidden;
    background: var(--stage-bg);
  }
  .banner {
    position: absolute;
    left: 36px;
    top: 300px;
    width: 1128px;
    height: 300px;
    background: var(--brand-green);
    overflow: hidden;
  }
  .head-illustration {
    position: absolute;
    left: 136px;
    top: 10px;
    width: 250px;
    height: 290px;
    border-radius: 125px 125px 0 0;
    background: linear-gradient(180deg, var(--art-light), var(--art-dark));
  }
  .savings-badge {
    position: absolute;
    left: 110px;
    top: 162px;
    width: 110px;
    height: 110px;
  }
  .headline {
    position: absolute;
    left: 466px;
    top: 40px;
    margin: 0;
    font-family: "Roboto Slab", Georgia, serif;
    font-weight: 400;
    font-size: 58px;
    line-height: 70px;
    color: var(--text-white);
  }
  .tagline {
    position: absolute;
    left: 466px;
    top: 204px;
    width: 417px;
    height: 50px;
    box-sizing: border-box;
    border-top: 1px dashed var(--line-green);
    border-bottom: 1px dashed var(--line-green);
    padding-left: 14px;
    font-family: "Carlito", "Calibri", sans-serif;
    font-weight: 700;
    font-size: 23px;
    line-height: 48px;
    letter-spacing: 0.8px;
    color: var(--deep-green);
    text-transform: uppercase;
  }
</style>
</head>
<body>
  <section class="banner">
    <div class="head-illustration" role="img" aria-label="Line drawing of a human head profile with a light bulb inside, symbolising smart energy thinking"></div>

    <svg class="savings-badge" viewBox="0 0 110 110" aria-label="Lower costs icon">
      <circle cx="52" cy="52" r="52" fill="var(--deep-green)"/>
      <circle cx="52" cy="52" r="43" fill="none" stroke="#ffffff" stroke-width="1" stroke-dasharray="2 2" opacity="0.6"/>
      <text x="52" y="74" text-anchor="middle" font-family="Roboto Slab, Georgia, serif" font-size="62" fill="#ffffff">$</text>
      <circle cx="90" cy="90" r="18" fill="#ffffff" stroke="var(--brand-green)" stroke-width="3"/>
      <path d="M90 80 V99 M82 91 L90 99 L98 91" fill="none" stroke="var(--deep-green)" stroke-width="3.5" stroke-linecap="round" stroke-linejoin="round"/>
    </svg>

    <h1 class="headline">Maintain High<br>Building Standards</h1>
    <p class="tagline">With lower energy costs</p>
  </section>
</body>
</html>
```